Heronwick Lodge Sign

Heronwick Lodge is a lake resort in Branson, MO
This resort used to have 66 units however the resort was sold in sections. I own the part of the resort that has all the amenities listed on the attached file. We need an updated sign and also billboard.
On a sign like this should be include a phone number?

```html
<!DOCTYPE html>
<html lang="en">
<head>
<meta charset="utf-8">
<title>Heronwick Lodge Billboard and Roadside Sign</title>
<link href="https://fonts.googleapis.com/css2?family=Montserrat:wght@400;500;700;800&family=Oswald:wght@300;500&display=swap" rel="stylesheet">
<style>
  :root {
    --navy: #0b3a78;
    --green: #6aab2e;
    --lime: #86bb2f;
    --yellow: #f3ea3a;
    --mint: #eaf6ee;
    --white: #ffffff;
    --page: #e6ebf0;
  }
  * { margin: 0; padding: 0; box-sizing: border-box; }
  html, body { width: 1200px; height: 1200px; overflow: hidden; background: var(--page); }
  body { position: relative; font-family: "Montserrat", sans-serif; color: var(--navy); }

  .billboard {
    position: absolute; left: 20px; top: 30px; width: 1160px; height: 620px;
    background: var(--mint); overflow: hidden;
  }
  .billboard-art { position: absolute; inset: 0; }
  .abs { position: absolute; white-space: nowrap; }

  .headline { left: 588px; top: 32px; font-size: 80px; font-weight: 800; letter-spacing: 1px; line-height: 1; }
  .resort-name { left: 592px; top: 116px; font-size: 56px; font-weight: 400; color: var(--green); line-height: 1; }
  .location { left: 594px; top: 184px; font-size: 26px; font-weight: 500; line-height: 1.2; }
  .amenities-title { left: 594px; top: 252px; font-size: 28px; font-weight: 800; line-height: 1.2; }
  .amenity-list { list-style: none; font-size: 15px; font-weight: 500; line-height: 20px; }
  .amenity-list li::before { content: "•"; color: var(--green); margin-right: 6px; }
  .list-a { left: 594px; top: 294px; }
  .list-b { left: 880px; top: 334px; }

  .call-label { left: 572px; top: 488px; font-size: 30px; font-weight: 800; color: var(--white); line-height: 1.2; }
  .call-number { left: 690px; top: 482px; font-size: 44px; font-weight: 800; color: var(--yellow); letter-spacing: 0.5px; line-height: 1.2; }
  .website { left: 612px; top: 552px; font-size: 34px; font-weight: 700; line-height: 1.2; }
  .website .tld { font-weight: 400; }

  .logo-name { left: 40px; top: 470px; font-size: 50px; font-weight: 800; color: var(--navy); }
  .logo-tag { left: 100px; top: 532px; font-size: 24px; font-weight: 700; color: var(--navy); }

  .road-sign {
    position: absolute; left: 60px; top: 700px; width: 300px; height: 440px;
    background: var(--mint); overflow: hidden; border: 1px solid #c9d6cc;
  }
  .sign-top {
    height: 150px; background: var(--navy); color: var(--white);
    display: flex; flex-direction: column; align-items: center; justify-content: center; gap: 6px;
    font-family: "Oswald", sans-serif;
  }
  .sign-brand { display: flex; align-items: center; gap: 10px; font-size: 30px; font-weight: 500; }
  .sign-dot { width: 18px; height: 18px; border-radius: 50%; background: var(--yellow); }
  .sign-sub { font-size: 14px; font-weight: 300; }
  .sign-welcome { font-family: "Oswald", sans-serif; text-align: center; padding-top: 22px; line-height: 1.1; }
  .sign-welcome .big { font-size: 46px; font-weight: 500; color: var(--navy); }
  .sign-welcome .small { font-size: 30px; font-weight: 300; color: var(--green); }
  .sign-call { position: absolute; left: 0; top: 320px; width: 300px; height: 56px; }
  .sign-call-text {
    position: absolute; left: 14px; top: 330px; font-family: "Oswald", sans-serif; color: var(--yellow);
    font-size: 26px; font-weight: 500; display: flex; align-items: center; gap: 6px;
  }
  .sign-call-text .lbl { font-size: 14px; color: var(--white); }
  .sign-web {
    position: absolute; left: 0; right: 0; top: 392px; text-align: center;
    font-family: "Oswald", sans-serif; font-size: 20px; font-weight: 300; color: var(--navy);
  }
</style>
</head>
<body>

<section class="billboard">
  <svg class="billboard-art" width="1160" height="620" viewBox="0 0 1160 620">
    <defs>
      <linearGradient id="houseTone" x1="0" y1="0" x2="1" y2="1">
        <stop offset="0" stop-color="#8fa27a"/>
        <stop offset="0.45" stop-color="#9a6a4a"/>
        <stop offset="1" stop-color="#c9d2bc"/>
      </linearGradient>
      <linearGradient id="catchTone" x1="0" y1="0" x2="0" y2="1">
        <stop offset="0" stop-color="#7f8f6a"/>
        <stop offset="1" stop-color="#b8b0a0"/>
      </linearGradient>
    </defs>
    <g role="img" aria-label="Photo of the lodge building with wooden balconies and a lakeside deck">
      <path d="M0 0 H470 C610 150 630 440 470 620 H0 Z" fill="url(#houseTone)"/>
    </g>
    <path d="M470 0 C610 150 630 440 470 620" fill="none" stroke="var(--navy)" stroke-width="3"/>
    <path d="M0 0 H200 C140 40 175 130 120 190 C90 225 40 215 0 230 Z" fill="var(--green)"/>
    <g role="img" aria-label="Photo of a young guest holding a large fish caught in the lake">
      <circle cx="450" cy="195" r="135" fill="url(#catchTone)" stroke="var(--green)" stroke-width="10"/>
    </g>
    <path d="M555 508 Q560 478 590 478 H1160 V538 H560 Z" fill="var(--lime)"/>
    <g transform="translate(636 482)">
      <path d="M8 6 C2 12 2 22 10 34 C18 46 28 54 38 56 C44 57 48 54 50 50 L42 40 C40 38 37 38 35 40 L31 44 C24 40 18 33 14 26 L18 22 C20 20 20 17 18 15 L10 6 Z" fill="var(--yellow)"/>
    </g>
    <path d="M1160 462 C1135 458 1118 480 1122 510 C1126 540 1110 580 1116 620 H1160 Z" fill="var(--navy)"/>
  </svg>

  <div class="abs headline">Welcome to</div>
  <div class="abs resort-name">Heronwick Lodge</div>
  <div class="abs location">located on Table Rock Lake<br>at Indian Point.</div>
  <div class="abs amenities-title">Amenities:</div>
  <ul class="abs amenity-list list-a">
    <li>Direct Lake access</li>
    <li>Swim Decks &amp; Slip Rentals</li>
    <li>Boat Rentals &amp; Indoor Pool</li>
    <li>Golf Carts</li>
    <li>Pontoon Boats</li>
    <li>Kayak - Paddleboards</li>
    <li>Family Reunions - Large Groups</li>
  </ul>
  <ul class="abs amenity-list list-b">
    <li>1-5 Bedroom Vacation Rentals</li>
    <li>Dining Hall</li>
    <li>Game Room</li>
    <li>Children's Activities</li>
    <li>Pet Friendly &amp; Gift Store</li>
    <li>Outdoor Games</li>
  </ul>

  <div class="abs call-label">Call</div>
  <div class="abs call-number">1-800-555-0142</div>
  <div class="abs website">www.heronwicklodge<span class="tld">.com</span></div>

  <div class="abs logo-name">Heronwick Lodge</div>
  <div class="abs logo-tag">on Table Rock Lake</div>
</section>

<section class="road-sign">
  <div class="sign-top">
    <div class="sign-brand"><span class="sign-dot"></span>Heronwick Lodge</div>
    <div class="sign-sub">on Table Rock Lake</div>
  </div>
  <div class="sign-welcome">
    <div class="big">Welcome to</div>
    <div class="small">Heronwick Lodge</div>
  </div>
  <svg class="sign-call" width="300" height="56" viewBox="0 0 300 56">
    <path d="M0 6 H262 V0 L298 28 L262 56 V50 H0 Z" fill="var(--lime)"/>
  </svg>
  <div class="sign-call-text">
    <span class="lbl">Call</span>
    <svg width="20" height="22" viewBox="0 0 56 60"><path d="M8 6 C2 12 2 22 10 34 C18 46 28 54 38 56 C44 57 48 54 50 50 L42 40 C40 38 37 38 35 40 L31 44 C24 40 18 33 14 26 L18 22 C20 20 20 17 18 15 L10 6 Z" fill="var(--yellow)"/></svg>
    1-800-555-0142
  </div>
  <div class="sign-web">www.heronwicklodge.com</div>
</section>

</body>
</html>
```